I am looking for help designing my new business cards. I would like rounded edges and a raised logo on the back of the card. I have 2 Logos. One with a boat in it and one without. I'd like the one on the back to be the one that includes the boat and just the name on the front. I have included multiple formats of my logo. Please let me know if you need anymore.

Target Market(s)

Potential buyers and other sales brokers

Industry/Entity Type

Sales - Yacht / Boat Sales

Contact Information for Business Card

Id liike the front to include just the business name portion of the logo along with my name (Corwin Dalby), phone number (555.318.6027), website address (www.dalbymarineco.example) and not my physical address but just "Charleston, SC". The back should include my full logo that has the boat included. This portion I'd prefer raised amd take up the majority of the space there. Thanks!!

Colors
0054AA
0677BA
7BADD7
CADEEF
E8F1F8
0094D4
00A9DD
6FCCEA
C7EBF8
E9F6FB

Requirements
Must have
• Double sided
Nice to have
• My email address: Corwin@dalbymarineco.example The NMTG logo somewhere small on the front of the card
Should not have
• My full address, prefer only "Charleston, SC"

```html
<!DOCTYPE html>
<html lang="en">
<head>
<meta charset="utf-8">
<title>Dalby Marine Co. — Business Card</title>
<link href="https://fonts.googleapis.com/css2?family=Montserrat:wght@400;600;800&display=swap" rel="stylesheet">
<style>
  :root {
    --navy: #33498b;
    --sky: #3b9fd8;
    --paper: #f7f7f5;
    --backdrop: #dedfe2;
  }
  * { margin: 0; padding: 0; box-sizing: border-box; }
  html, body {
    width: 1200px;
    height: 900px;
    overflow: hidden;
    background: var(--backdrop);
    font-family: "Montserrat", sans-serif;
  }
  .sheet {
    width: 1200px;
    height: 900px;
    display: flex;
    align-items: center;
    justify-content: center;
    gap: 60px;
  }
  .card {
    position: relative;
    width: 520px;
    height: 300px;
    background: var(--paper);
    border-radius: 26px;
    box-shadow: 0 2px 0 #e9e9e9, 0 4px 0 #e2e2e2, 0 6px 0 #dcdcdc, 0 14px 28px rgba(0,0,0,0.12);
  }

  /* Front */
  .brand-name {
    position: absolute;
    left: 38px;
    top: 40px;
    font-weight: 800;
    font-size: 26px;
    letter-spacing: 1px;
    color: var(--navy);
    text-transform: uppercase;
    white-space: nowrap;
  }
  .owner-name {
    position: absolute;
    left: 38px;
    top: 82px;
    font-weight: 600;
    font-size: 20px;
    color: var(--navy);
    white-space: nowrap;
  }
  .contact-list {
    position: absolute;
    right: 32px;
    bottom: 34px;
    list-style: none;
    display: flex;
    flex-direction: column;
    gap: 7px;
  }
  .contact-item {
    display: flex;
    align-items: center;
    gap: 9px;
    font-size: 13px;
    color: var(--navy);
    white-space: nowrap;
  }
  .contact-icon {
    width: 18px;
    height: 18px;
    flex: none;
    background: var(--navy);
    border-radius: 2px;
    display: flex;
    align-items: center;
    justify-content: center;
  }
  .contact-icon svg { width: 12px; height: 12px; }

  /* Back */
  .card-back {
    display: flex;
    align-items: center;
    justify-content: center;
  }
  .brand-name-large {
    font-weight: 800;
    font-size: 40px;
    letter-spacing: 2px;
    color: var(--navy);
    text-transform: uppercase;
    white-space: nowrap;
  }
</style>
</head>
<body>
<main class="sheet">
  <section class="card card-front" aria-label="Card front">
    <div class="brand-name">Dalby Marine Co.</div>
    <div class="owner-name">Corwin Dalby</div>
    <ul class="contact-list">
      <li class="contact-item">
        <span class="contact-icon">
          <svg viewBox="0 0 12 12"><path d="M6 1a3.3 3.3 0 0 0-3.3 3.3C2.7 7 6 11 6 11s3.3-4 3.3-6.7A3.3 3.3 0 0 0 6 1z" fill="#fff"/><circle cx="6" cy="4.3" r="1.2" fill="var(--navy)"/></svg>
        </span>
        Port Selby, GA.
      </li>
      <li class="contact-item">
        <span class="contact-icon">
          <svg viewBox="0 0 12 12"><path d="M3 1.2l1.6 2.2-1 1.1c.6 1.4 1.6 2.4 3 3l1.1-1 2.2 1.6-1 1.8C5.6 9.9 2.1 6.4 1.2 3z" fill="#fff"/></svg>
        </span>
        555.318.6027
      </li>
      <li class="contact-item">
        <span class="contact-icon">
          <svg viewBox="0 0 12 12"><rect x="1.5" y="3" width="9" height="6" fill="none" stroke="#fff" stroke-width="1"/><path d="M1.5 3L6 6.6 10.5 3" fill="none" stroke="#fff" stroke-width="1"/></svg>
        </span>
        Corwin@dalbymarineco.example
      </li>
      <li class="contact-item">
        <span class="contact-icon">
          <svg viewBox="0 0 12 12" fill="none" stroke="#fff" stroke-width="0.9"><circle cx="6" cy="6" r="4.5"/><ellipse cx="6" cy="6" rx="2" ry="4.5"/><path d="M1.5 6h9M2.3 3.7h7.4M2.3 8.3h7.4"/></svg>
        </span>
        www.dalbymarineco.example
      </li>
    </ul>
  </section>

  <section class="card card-back" aria-label="Card back">
    <div class="brand-name-large">Dalby Marine Co.</div>
  </section>
</main>
</body>
</html>
```